VELD 20th Anniversary Letterhead

VELD – Guidance, Outreach, and Practice – is Brightmoor Holdings’s premiere Frontline Associate training program. VELD includes compliance training, professional development, skill building, and training for corporate and sector-specific initiatives for all Brightmoor Holdings Frontline Associates.

We are celebrating our 20th anniversary in 2017! We would like our letterhead and logo to include some nod to this 20th anniversary. We're open to ideas that showcases this great milestone for the program. We will use this letterhead to showcase our anniversary in multiple training and marketing mediums throughout the year.

Logo: We would like to include our current logo with something to call out our 20th anniversary; we won't need a totally new logo from scratch. This logo should go at the top of the letterhead. We will need to include the Brightmoor Holdings/Onward Together logo in the footer of the letterhead. It can be smaller though.

Letterhead: This letterhead will be used both in portrait and landscape on 8 1/2 X 11 paper. Often we use this letterhead in PowerPoint for slides, as well as in a lesson plan. We need to include enough space write a title in the header.

We are open to a watermark, but would love to see letterheads with and without it.

I have included our current template and two logos (that should be used).
Updates

Project Deadline Extended
Reason: We would like to extend the deadline for this project to allow for more submissions and/or revision to current submissions. We are most interested in designs that include something about our 20th anniversary (1997 - 2017) in either our logo, the header/footer, or in a watermark.

Target Market(s)

Frontline Associates (hourly associates), Managers

Industry/Entity Type

Communication

Logo Text

VELD 20th Anniversary

Font styles to use
Other font styles liked:
• Calibri; Century Gothic

Colors
6b449b
000000
cbcbcb

Requirements
Must have
• - Appropriate for web and print
• - EPS, JPEG, PNG
• - Purple (from the VELD logo), black, and gray color scheme
• - Transparent
• - Space to put a title in the header
• - No more than 1 inch from the top
• - Portrait and Landscape to use on letterhead and PowerPoint
Nice to have
• - Maybe a watermark? <-- We are open to seeing designs with and without it.
• - Should look good when printed in color or black and white
Should not have
• - No stock images, clip art
• - Overly large graphics that take up too much space in the body of the letterhead. We will need to create text here.

```html
<!DOCTYPE html>
<html lang="en">
<head>
<meta charset="utf-8">
<title>VELD 20th Anniversary Letterhead</title>
<link rel="stylesheet" href="https://fonts.googleapis.com/css2?family=Open+Sans:wght@400;600;700&display=swap">
<style>
  :root {
    --purple: #3f2478;
    --ink: #2b2b2b;
    --gray: #cbcbcb;
    --page: #eeeeef;
    --backdrop: #f3f3f5;
    --white: #ffffff;
  }
  html, body {
    margin: 0;
    padding: 0;
    width: 807px;
    height: 1200px;
    overflow: hidden;
    background: var(--backdrop);
    font-family: "Open Sans", Arial, sans-serif;
  }
  .canvas {
    position: relative;
    width: 807px;
    height: 1200px;
  }
  .letterhead {
    position: absolute;
    left: 34px;
    top: 371px;
    width: 738px;
    height: 458px;
    background: var(--page);
    overflow: hidden;
  }
  .swoop {
    position: absolute;
    inset: 0;
  }
  .brand {
    position: absolute;
    left: 72px;
    top: 68px;
    display: flex;
    align-items: center;
    gap: 10px;
  }
  .brand-mark {
    width: 12px;
    height: 12px;
    background: var(--purple);
  }
  .brand-name {
    font-size: 40px;
    font-weight: 600;
    letter-spacing: 3px;
    color: var(--purple);
    line-height: 1;
  }
  .brand-tagline {
    position: absolute;
    left: 74px;
    top: 116px;
    font-size: 8px;
    font-weight: 600;
    letter-spacing: 1px;
    text-transform: uppercase;
    color: var(--ink);
  }
  .anniversary {
    position: absolute;
    right: 60px;
    top: 66px;
    display: flex;
    align-items: center;
    gap: 8px;
  }
  .anniversary-dot {
    width: 10px;
    height: 10px;
    border-radius: 50%;
    background: var(--purple);
  }
  .anniversary-name {
    font-size: 16px;
    font-weight: 600;
    color: var(--purple);
    line-height: 1;
  }
  .body-text {
    position: absolute;
    left: 197px;
    top: 198px;
    margin: 0;
    padding: 0;
    list-style: none;
    font-size: 18px;
    font-weight: 700;
    line-height: 22px;
    color: var(--ink);
  }
  .body-text li::before { content: "-  "; white-space: pre; }
  .footer-brand {
    position: absolute;
    left: 28px;
    top: 433px;
    font-size: 9px;
    font-weight: 600;
    color: var(--white);
  }
  .footer-contact {
    position: absolute;
    right: 30px;
    top: 414px;
    display: flex;
    align-items: center;
    gap: 12px;
    color: var(--white);
    font-size: 6.5px;
    line-height: 9.5px;
  }
  .address { text-align: right; }
  .contact-lines { text-align: left; }
  .contact-icons { display: flex; flex-direction: column; gap: 1.5px; }
</style>
</head>
<body>
<main class="canvas">
  <section class="letterhead">
    <svg class="swoop" width="738" height="458" viewBox="0 0 738 458" aria-hidden="true">
      <path d="M738,372 C600,408 420,424 330,420 C120,410 20,330 37,265" fill="none" stroke="var(--gray)" stroke-width="5"/>
      <path d="M127,137 C70,175 10,215 0,232 L0,458 L738,458 L738,377 C600,412 420,428 330,424 C120,414 20,332 37,265 C48,225 90,170 127,137 Z" fill="var(--purple)"/>
    </svg>

    <div class="brand">
      <span class="brand-mark"></span>
      <span class="brand-name">VELD</span>
    </div>
    <div class="brand-tagline">Guidance, Outreach, and Practice</div>

    <div class="anniversary">
      <span class="anniversary-dot"></span>
      <span class="anniversary-name">VELD 20th Anniversary</span>
    </div>

    <ul class="body-text">
      <li>first line of you text is here</li>
      <li>first line of you text is here</li>
      <li>first line of you text is here</li>
      <li>first line of you text is here</li>
    </ul>

    <div class="footer-brand">Brightmoor Holdings | Onward Together</div>

    <div class="footer-contact">
      <div class="address">Harrow Lane Suite 120,<br>Fernvale, CA 90000</div>
      <svg width="7" height="9" viewBox="0 0 7 9" aria-hidden="true">
        <path d="M3.5,0 C5.5,0 7,1.5 7,3.4 C7,5.6 3.5,9 3.5,9 C3.5,9 0,5.6 0,3.4 C0,1.5 1.5,0 3.5,0 Z" fill="var(--white)"/>
        <circle cx="3.5" cy="3.4" r="1.3" fill="var(--purple)"/>
      </svg>
      <div class="contact-lines">555-010-2000<br>555-010-2700<br>www.veldtraining.org</div>
      <div class="contact-icons">
        <svg width="8" height="8" viewBox="0 0 8 8" aria-hidden="true">
          <path d="M1.5,0.5 L3,0.5 L3.6,2.3 L2.6,3 C3,4 4,5 5,5.4 L5.7,4.4 L7.5,5 L7.5,6.5 C7.5,7.2 7,7.5 6.4,7.5 C3.3,7.3 0.7,4.7 0.5,1.6 C0.5,1 0.8,0.5 1.5,0.5 Z" fill="var(--white)"/>
        </svg>
        <svg width="8" height="8" viewBox="0 0 8 8" aria-hidden="true">
          <rect x="2" y="0.5" width="4" height="2" fill="var(--white)"/>
          <rect x="0.5" y="2.8" width="7" height="3" rx="0.6" fill="var(--white)"/>
          <rect x="2" y="5" width="4" height="2.5" fill="var(--white)"/>
        </svg>
        <svg width="8" height="8" viewBox="0 0 8 8" aria-hidden="true">
          <circle cx="4" cy="4" r="3.4" fill="none" stroke="var(--white)" stroke-width="0.8"/>
          <ellipse cx="4" cy="4" rx="1.5" ry="3.4" fill="none" stroke="var(--white)" stroke-width="0.6"/>
          <line x1="0.6" y1="4" x2="7.4" y2="4" stroke="var(--white)" stroke-width="0.6"/>
        </svg>
      </div>
    </div>
  </section>
</main>
</body>
</html>
```